Lawn Maintenance Company needs attractive add for local newspaper

My company Fennick Yard Service offers many lawn and yard services but I want this add to focus on one specific service we offer.
- Lawn Fertilizer and Weed Control -

This will be an add for our local newspaper, likely a 1/4 page

Some more information about this service.
Our customers generally call us when their lawn is over run with weeds or is performing poorly. Most of the time we set them up with a program and we return to their property every 4 - 5 weeks for another application. 95% of our customers return the following year for the same program. If the customer wishes we will also do a one time application

email: fennickyardservice@example.net
phone: call or text 555-418-7390

Target Market(s)

- Local small towns, populations less than 20,000
- Residential and Commercial customers with lawns
- People who are using the competitors service and aren't happy with it

Industry/Entity Type

Lawn Care

Requirements
Must have
• Must include our logo, email address and phone number
• - Logo
• - Email address and phone number (call or text)
• - Must focus on the service we want to sell (fertilizer and weed control)
Nice to have
• Some phrases or words that should be included, does not need to be word for word as long as the point is made
• - We service both Residential & Commercial properties
• - We offer professional service that can dramatically improve your lawn whether you are looking for a single application or a season long fertilizer/weed control program
• - Our lawn techs are licensed and certified applicators
Should not have
• I do not want any stock pictures of people, houses or equipment.

```html
<!DOCTYPE html>
<html lang="en">
<head>
<meta charset="utf-8">
<title>Fennick Yard Service – Weed Control &amp; Fertilizers</title>
<link href="https://fonts.googleapis.com/css2?family=Open+Sans:wght@700;800&family=PT+Sans+Narrow:wght@400;700&display=swap" rel="stylesheet">
<style>
  :root {
    --paper: #ffffff;
    --tile: #b9d36b;
    --leaf: #7cb844;
    --pale: #d3e39f;
    --bark: #76311e;
    --rust: #c5441a;
    --grass-dark: #2f5a22;
    --grass-mid: #4d7c35;
    --ink: #4d6a2a;
    --brand: #2f7d32;
  }
  html, body {
    margin: 0;
    padding: 0;
    width: 1133px;
    height: 1200px;
    overflow: hidden;
    background: var(--paper);
  }
  .ad {
    position: relative;
    width: 1133px;
    height: 1200px;
    overflow: hidden;
    background: var(--paper);
  }
  .tile-field {
    position: absolute;
    left: 0;
    top: 0;
  }

  /* main rotated board of four-plus squares */
  .board-clip {
    position: absolute;
    left: 0;
    top: 100px;
    width: 1133px;
    height: 1100px;
    overflow: hidden;
  }
  .service-board {
    position: absolute;
    left: 153px;
    top: 45px;
    width: 560px;
    height: 840px;
    transform: rotate(-9.5deg);
    transform-origin: 0 0;
  }
  .cell {
    position: absolute;
    width: 280px;
    height: 280px;
  }
  .cell--weed { left: 0; top: 0; background: var(--leaf); }
  .cell--grass-top { left: 280px; top: 0; }
  .cell--brand { left: 0; top: 280px; background: var(--paper); }
  .cell--fert { left: 280px; top: 280px; background: var(--bark); }
  .cell--grass-bottom { left: 0; top: 560px; }
  .grass {
    background:
      radial-gradient(ellipse at 35% 40%, rgba(255,255,255,0.07), transparent 60%),
      linear-gradient(160deg, var(--grass-mid), var(--grass-dark));
  }

  .weed-title {
    position: absolute;
    left: 28px;
    top: 114px;
    margin: 0;
    font-family: "Open Sans", sans-serif;
    color: var(--rust);
    line-height: 1;
    white-space: nowrap;
  }
  .weed-title__big {
    display: block;
    font-size: 84px;
    font-weight: 800;
    letter-spacing: -4px;
  }
  .weed-title__small {
    display: block;
    font-size: 44px;
    font-weight: 700;
    letter-spacing: -2px;
    margin-left: 14px;
  }

  .fert-title {
    position: absolute;
    left: 0;
    top: 34px;
    margin: 0;
    font-family: "Open Sans", sans-serif;
    font-weight: 800;
    color: var(--paper);
    font-size: 63px;
    letter-spacing: -3px;
    line-height: 50px;
    white-space: nowrap;
  }
  .fert-title span { display: block; }
  .fert-title .s1 { margin-left: 50px; }
  .fert-title .s2 { margin-left: 59px; }
  .fert-title .s3 { margin-left: 111px; }
  .fert-title .s4 { margin-left: 102px; }

  .brand-mark {
    position: absolute;
    inset: 0;
    display: flex;
    align-items: center;
    justify-content: center;
    gap: 10px;
  }
  .brand-mark__square {
    flex: none;
    width: 24px;
    height: 24px;
    background: var(--brand);
  }
  .brand-mark__name {
    font-family: "PT Sans Narrow", sans-serif;
    font-weight: 700;
    font-size: 34px;
    color: var(--brand);
    line-height: 1;
    width: 150px;
  }

  /* repeated panel bleeding off the right edge */
  .side-clip {
    position: absolute;
    left: 0;
    top: 0;
    width: 998px;
    height: 1200px;
    overflow: hidden;
  }
  .side-panel {
    position: absolute;
    left: 810px;
    top: 315px;
    width: 300px;
    height: 277px;
    background: var(--pale);
    transform: rotate(-9.5deg);
    transform-origin: 0 0;
  }
  .side-panel .weed-title { left: 34px; top: 120px; }

  .info-card {
    position: absolute;
    left: 364px;
    top: 745px;
    width: 555px;
    height: 280px;
    background: var(--pale);
    transform: rotate(-9.7deg);
    transform-origin: 0 0;
    box-sizing: border-box;
    padding: 32px 0 0 18px;
  }
  .info-list {
    margin: 0;
    padding: 0;
    list-style: none;
    font-family: "PT Sans Narrow", sans-serif;
    font-size: 26px;
    line-height: 32px;
    color: var(--ink);
    white-space: nowrap;
  }
  .info-list li {
    padding-left: 13px;
    text-indent: -13px;
  }
  .info-list li::before { content: "- "; }

  .contact {
    position: absolute;
    left: 608px;
    top: 1006px;
    margin: 0;
    font-style: normal;
    transform: rotate(-10.5deg);
    transform-origin: 0 0;
    font-family: "PT Sans Narrow", sans-serif;
    color: var(--ink);
    white-space: nowrap;
  }
  .contact__email {
    display: block;
    font-size: 26px;
    line-height: 30px;
  }
  .contact__phone {
    display: block;
    font-size: 32px;
    line-height: 36px;
    font-weight: 700;
    margin-left: 44px;
  }
</style>
</head>
<body>
<main class="ad">
  <svg class="tile-field" width="1133" height="1200" viewBox="0 0 1133 1200" aria-hidden="true">
    <rect x="118" y="102" width="875" height="1003" fill="var(--tile)"/>
    <g stroke="var(--paper)" stroke-width="4">
      <line x1="118" y1="176" x2="230" y2="176"/>
      <line x1="118" y1="290" x2="230" y2="290"/>
      <line x1="118" y1="404" x2="230" y2="404"/>
      <line x1="118" y1="512" x2="230" y2="512"/>
      <line x1="118" y1="624" x2="270" y2="624"/>
      <line x1="118" y1="728" x2="270" y2="728"/>
      <line x1="118" y1="830" x2="270" y2="830"/>
      <line x1="118" y1="930" x2="270" y2="930"/>
      <line x1="228" y1="102" x2="228" y2="520"/>
      <line x1="700" y1="192" x2="993" y2="192"/>
      <line x1="700" y1="296" x2="993" y2="296"/>
      <line x1="886" y1="102" x2="886" y2="296"/>
      <line x1="560" y1="640" x2="993" y2="640"/>
      <line x1="780" y1="590" x2="780" y2="700"/>
      <line x1="900" y1="730" x2="993" y2="730"/>
      <line x1="900" y1="934" x2="993" y2="934"/>
      <line x1="118" y1="1075" x2="993" y2="1075"/>
      <line x1="340" y1="1075" x2="340" y2="1105"/>
      <line x1="448" y1="1000" x2="448" y2="1105"/>
      <line x1="886" y1="1075" x2="886" y2="1105"/>
    </g>
  </svg>

  <div class="side-clip">
    <div class="side-panel">
      <p class="weed-title" aria-hidden="true">
        <span class="weed-title__big">weed</span>
        <span class="weed-title__small">CONTROL</span>
      </p>
    </div>
  </div>

  <div class="board-clip">
    <section class="service-board">
      <div class="cell cell--grass-top grass" role="img" aria-label="Close-up of healthy green lawn grass"></div>
      <div class="cell cell--weed">
        <h1 class="weed-title">
          <span class="weed-title__big">weed</span>
          <span class="weed-title__small">CONTROL</span>
        </h1>
      </div>
      <div class="cell cell--brand">
        <div class="brand-mark">
          <span class="brand-mark__square"></span>
          <span class="brand-mark__name">Fennick Yard Service</span>
        </div>
      </div>
      <div class="cell cell--fert">
        <h2 class="fert-title" aria-label="Fertilizers">
          <span class="s1">FER</span>
          <span class="s2">TI</span>
          <span class="s3">LI</span>
          <span class="s4">ZERS</span>
        </h2>
      </div>
      <div class="cell cell--grass-bottom grass" role="img" aria-label="Close-up of healthy green lawn grass"></div>
    </section>
  </div>

  <section class="info-card">
    <ul class="info-list">
      <li>We service both Residential &amp; Commercial properties</li>
      <li>We offer professional service that can dramatically<br>improve your lawn whether you are looking<br>for a single application or a season<br>long fertilizer/weed control program</li>
      <li>Our lawn techs are licensed and certified applicators</li>
    </ul>
  </section>

  <address class="contact">
    <span class="contact__email">fennickyardservice@example.net</span>
    <span class="contact__phone">555-418-7390</span>
  </address>
</main>
</body>
</html>
```